Kestrel Dental personal information forms

We are a Dental Practice that require an update to our information forms, there are 3 versions of it.
I will attach our old ones, we need to keep the same information on there, we just want them to look better and use our current logo and colours.
Our website is www.kestreldental.net
Our facebook is www.friendnook.com/kestreldentalbrookplaza/
..................................................................................................

Target Market(s)

Everyone, easy to read

Industry/Entity Type

Dental Clinic

Colors
0692cd
34a6d7
cee9f5
ffffff
0255a3
3276b5

Requirements
Must have
• Logo
• Our colours
• same information as the uploaded versions
Should not have
• any other colour besides the blues, black and white

```html
<!DOCTYPE html>
<html lang="en">
<head>
<meta charset="utf-8">
<title>Kestrel Dental – Information Update Form pg. 2</title>
<link href="https://fonts.googleapis.com/css2?family=Mulish:ital,wght@0,400;0,500;0,700;0,800;1,400;1,700&display=swap" rel="stylesheet">
<style>
  :root{
    --blue-bright:#0692cd;
    --blue-sky:#34a6d7;
    --blue-pale:#cee9f5;
    --blue-deep:#0255a3;
    --blue-mid:#3276b5;
    --ink:#1a1a1a;
    --rule:#2a2a2a;
    --white:#ffffff;
  }
  *{box-sizing:border-box;margin:0;padding:0}
  html,body{width:927px;height:1200px;overflow:hidden}
  body{
    font-family:"Mulish",Arial,sans-serif;
    color:var(--ink);
    background:linear-gradient(180deg,var(--white) 18%,var(--white) 70%,#e6f2f9 100%);
    position:relative;
  }
  .header-band{
    position:absolute;left:0;top:0;width:927px;height:190px;
    background:linear-gradient(180deg,#d9ecf7 0%,#eef7fc 55%,var(--white) 100%);
  }
  .brand{
    position:absolute;right:27px;top:58px;
    display:flex;align-items:center;gap:14px;
    color:var(--blue-bright);font-weight:500;font-size:54px;line-height:1;
  }
  .brand__dot{width:18px;height:18px;border-radius:50%;background:var(--blue-bright)}
  .abs{position:absolute}
  .practitioners{
    left:27px;top:218px;color:var(--blue-mid);font-style:italic;
    font-size:24px;line-height:31px;
  }
  .form-tag{right:27px;top:258px;color:var(--blue-bright);font-size:14px;letter-spacing:.5px}
  .form-tag b{font-size:19px;font-weight:800;margin-left:4px}
  .welcome{left:27px;top:322px;color:var(--blue-bright);font-size:23px;font-weight:500}
  .intro{left:27px;top:360px;width:873px;font-size:16.8px;line-height:21.3px}
  .intro b{font-weight:700}
  .question{
    left:27px;width:873px;font-size:17.4px;line-height:21.7px;
    display:flex;justify-content:space-between;align-items:flex-end;
    padding-bottom:10px;border-bottom:1.3px solid var(--rule);
  }
  .question .yn{font-weight:800;white-space:nowrap}
  .q-meds{top:477px}
  .q-allergy{top:548px}
  .q-other{top:834px}
  .q-surgery{top:891px}
  .q-preg{top:950px}
  .checklist-title{left:27px;top:604px;font-size:17.4px}
  .checklist-title b{font-weight:800}
  .conditions{
    left:27px;top:636px;width:873px;list-style:none;
    display:grid;grid-template-columns:218px 218px 218px 218px;
    grid-auto-flow:column;grid-template-rows:repeat(6,30.3px);
    font-size:17.4px;
  }
  .conditions li{display:flex;align-items:center;gap:9px}
  .conditions li::before{content:"";width:11px;height:11px;border:1px solid var(--ink);flex:none}
  .conditions .col4{grid-column:4}
  .declaration{left:27px;top:1008px;width:873px;font-size:13.2px;line-height:19px}
  .declaration em{font-weight:700}
  .signature{
    left:27px;top:1152px;width:873px;font-size:17.4px;
    display:flex;align-items:flex-end;white-space:nowrap;
  }
  .signature .line{border-bottom:1.2px solid var(--rule);height:17px}
  .signature .line--sign{flex:0 0 335px;margin-left:4px}
  .signature .line--date{flex:1 1 auto;margin-left:4px}
  .signature .date-label{margin-left:10px}
</style>
</head>
<body>
  <div class="header-band" role="img" aria-label="Soft blue wave band across the top of the form"></div>

  <div class="brand">
    <span class="brand__dot"></span>
    <span class="brand__name">Kestrel Dental</span>
  </div>

  <p class="abs practitioners">Dr. Peter Halloran &amp; Dr. Simon Ashcroft<br>Dental Surgeons</p>
  <p class="abs form-tag">INFORMATION UPDATE FORM <b>pg. 2</b></p>

  <h1 class="abs welcome">WELCOME BACK TO OUR PRACTICE!</h1>
  <p class="abs intro"><b><i>This information is confidential</i></b> and is necessary to enable us to offer you <b><i>the best possible care</i></b>. Because we haven’t seen you in some time and because we care about your health status, please take your time and thoroughly complete the following update of your personal and medical information. It is <b><i>essential</i></b> that we know about your past and present medical history. Many medical conditions may interfere with dental procedures.</p>

  <div class="abs question q-meds"><span>Are you currently or have you taken any prescribed medication or dietary supplements in<br>the last 12 months? (If yes, please list below.)</span><span class="yn">YES/NO</span></div>
  <div class="abs question q-allergy"><span>Allergies/Reactions? If yes, please list below.</span><span class="yn">YES/NO</span></div>

  <p class="abs checklist-title">Have you <b>ever had</b> or are you <b>suffering</b> from any of the following? Please tick any that apply:</p>
  <ul class="abs conditions">
    <li>Rheumatic fever</li><li>Epilepsy</li><li>Asthma</li><li>Tuberculosis</li><li>Radiation Therapy</li><li>Dizziness, fainting</li>
    <li>Hepatitis A B or C</li><li>Diabetes</li><li>Kidney Disease</li><li>Heart Attack</li><li>High Blood Pressure</li><li>Bleeding problems</li>
    <li>Artificial joints</li><li>Respiratory problems</li><li>HIV Positive</li><li>High Cholesterol</li><li>Cancer</li><li>Pace-maker</li>
    <li class="col4">Osteoporosis</li><li class="col4">Heart rate problems</li><li class="col4">Heart murmur</li>
  </ul>

  <div class="abs question q-other"><span>Do you have any disease, condition or problem not listed above? (If yes, please give details).</span><span class="yn">YES/NO</span></div>
  <div class="abs question q-surgery"><span>Have you had surgery or been to hospital in the last 5 years? (If yes, please give details).</span><span class="yn">YES/NO</span></div>
  <div class="abs question q-preg"><span>For women: Are you pregnant? If yes, how many months?</span><span class="yn">YES/NO</span></div>

  <p class="abs declaration"><em><i>The information above that I have provided is to the best of my knowledge true and correct and I understand that it is my responsibility to inform of any changes in my medical status.</i></em> This is to certify that I, the undersigned, consent to the performing of the dental and oral surgery procedures agreed to be necessary or advisable, including the use of local anaesthetic as indicated and I will assume responsibility for the fees associated with these procedures. Therefore, I shall pay any legal costs, including solicitor and own costs, tracing costs and any collection commission incurred by Kestrel Dental as a result of my failure to pay any amount due to Kestrel Dental.</p>

  <div class="abs signature">
    <span>Patient/Parent/Person Responsible Signature:</span>
    <span class="line line--sign"></span>
    <span class="date-label">Date:</span>
    <span class="line line--date"></span>
  </div>
</body>
</html>
```